Renewable Energy Consultancy needs relatively simple but smart website

We are a renewable energy focussed consultancy called Bellmoran, and we are just starting out. Our target is to bring knowledge of the detailed technical and commercial operations of renewables projects, mainly wind energy.

Our target customers are major energy utilities and private finance groups, who look to invest in renewables projects as a long term money-earning system. We are a fairly young, dynamic team of industry-respected people (4 of us) but we need to make ourselves look bigger than this (our customers will expect us to take on major projects, so we need to look big enough to handle it...)

We're not going to sell anything from our website and we expect it to just support our company name. Most of our customers are made by strong networks and relationships, so its mainly there to give confidence in our capabilities and give a strong view of who we are. We probably need a site with 4/5 pages which we can then expand when needed.

We have logos and headers (attached) which we want to use (also run through artpitchly), and I've attached a few pictures of projects similar to those we will be involved in to give us a feel for how it will look. Also attached are the colours we liked which are now used in the logo, and the font details. Whilst we're a "green" company with a "green" logo, we don't want to be completely green, so some nice combinations of colours on the pages would be good.

Ideally we need to have chirpnet/workgrid news feeds somewhere linked into the site.

The design should be smart - giving a feel of high integrity and assurance whilst making us seem approachable and knowledgeable.

Target Market(s)

Renewables investors, developers of renewables projects (wind farms etc),

Industry/Entity Type

Finance

Coding

Coded - Design and coding required

Number of Pages Required

4 page

Other font styles liked:
• See the attachment with brand text/colour details ("colour codes" filename)

Requirements
Must have
• A fairly simple, but smart website design. We're looking to provide confidence and consolidate our networks with the website, not specifically find new customers - so its really just to give customers somewhere they can relate to online
Nice to have
• We have logos/brands and colours - so a website which incorperates these well and brings accross a professional company
• Would be nice to have a page (such as a blog/wordpress) we can easily update with news/events etc and links to chirpnet feed and workgrid feed ideally.
Should not have
• cartoons, flashy gimmicks,

```html
<!DOCTYPE html>
<html lang="en">
<head>
<meta charset="utf-8">
<title>Bellmoran — Renewable Energy Consultancy</title>
<link rel="stylesheet" href="https://fonts.googleapis.com/css2?family=Figtree:wght@400;500;600;700&family=Lato:wght@300;400;700;900&display=swap">
<style>
:root{
  --green:#72b100;
  --green-dark:#5f9400;
  --link-green:#2f6a00;
  --ink:#222;
  --text:#555;
  --rule:#cfcfcf;
  --footer:#161616;
  --footer-bottom:#0f0f0f;
  --footer-text:#b3b3b3;
  --white:#fff;
}
*{margin:0;padding:0;box-sizing:border-box}
html,body{width:1046px;height:1200px;overflow:hidden;background:var(--white)}
body{font-family:"Figtree",sans-serif;color:var(--text)}
.page{position:relative;width:1200px;height:1377px;transform:scale(0.871667);transform-origin:0 0}
.abs{position:absolute}

/* header */
.brand{position:absolute;display:flex;align-items:center;gap:38px}
.brand-dot{border-radius:50%;background:var(--green)}
.brand-name{font-family:"Figtree",sans-serif;font-weight:400;letter-spacing:2px}
.site-header .brand{left:110px;top:30px}
.site-header .brand-dot{width:57px;height:57px}
.site-header .brand-name{font-size:48px;color:#555}
.call{position:absolute;left:870px;top:36px}
.call svg{position:absolute;left:0;top:4px}
.call-label{position:absolute;left:54px;top:0;font-size:17px;color:var(--ink);white-space:nowrap;font-weight:500}
.call-number{position:absolute;left:54px;top:19px;font-size:26px;font-weight:700;color:var(--green);white-space:nowrap}

/* nav */
.main-nav{position:absolute;left:0;top:122px;width:1200px;height:57px;background:var(--green);font-family:"Lato",sans-serif}
.nav-item{position:absolute;top:17px;font-size:16px;color:var(--white)}
.nav-item.active{left:112px;top:13px;width:61px;height:30px;background:#222;border-radius:2px;text-align:center;line-height:30px}
.nav-sep{position:absolute;top:12px;width:1px;height:34px;background:rgba(255,255,255,.28)}
.follow{position:absolute;left:884px;top:15px;font-size:19px;color:var(--white)}
.social{position:absolute;top:12px;width:29px;height:29px;border-radius:50%;background:#1a1a1a}

/* hero */
.hero{position:absolute;left:0;top:179px;width:1200px;height:464px;
  background:linear-gradient(180deg,#3b4a63 0%,#6d5a73 25%,#c77a64 48%,#e8a56a 62%,#6b4a3c 80%,#121212 100%)}
.hero-title{position:absolute;left:0;top:144px;width:1200px;text-align:center;font-family:"Lato",sans-serif;
  font-weight:300;font-size:42px;line-height:47px;color:var(--white);text-shadow:0 1px 3px rgba(0,0,0,.35)}
.hero-title b{font-weight:900}

/* content */
.section-title{position:absolute;top:680px;font-size:21px;font-weight:600;color:#333;text-transform:uppercase}
.section-title span{color:var(--green)}
.section-rule{position:absolute;top:716px;height:1px;background:var(--rule)}
.section-rule::before{content:"";position:absolute;left:0;top:-1px;width:52px;height:3px;background:#222}
.photo{position:absolute}
.body-copy{position:absolute;font-size:14.5px;line-height:21.5px;color:var(--text)}
.btn{position:absolute;left:122px;top:979px;width:104px;height:30px;background:var(--green);color:var(--white);font-size:16px;line-height:30px;text-align:center}
.btn::before{content:"";position:absolute;left:16px;top:-6px;border:6px solid transparent;border-top:0;border-bottom-color:var(--green)}
.post-title{position:absolute;left:436px;font-size:21px;font-weight:500;color:var(--green)}
.read-more{position:absolute;left:435px;font-size:14.5px;color:var(--link-green);text-decoration:underline;text-underline-offset:3px}
.project-card{position:absolute;left:767px;top:741px;width:317px;height:261px;border:1px solid #ddd}
.project-title{position:absolute;left:779px;top:874px;font-size:17px;color:var(--green)}
.pager{position:absolute;left:768px;top:967px;width:315px;height:34px;display:flex;gap:1px;background:#fff}
.pager div{height:34px;display:flex;align-items:center;justify-content:center;font-size:18px;font-weight:700;color:var(--white)}
.pager .arrow{width:45px;background:#222}
.pager .num{width:44px;background:var(--green)}
.pager .num.current::before{content:"";position:absolute;margin-top:-40px;border:6px solid transparent;border-top:0;border-bottom-color:var(--green)}

/* footer */
.site-footer{position:absolute;left:0;top:1049px;width:1200px;height:269px;background:var(--footer)}
.foot-title{position:absolute;top:30px;font-size:17px;font-weight:500;color:var(--white)}
.foot-rule{position:absolute;top:67px;height:1px;background:#3a3a3a}
.foot-rule::before{content:"";position:absolute;left:0;top:-2px;width:54px;height:4px;background:var(--green)}
.foot-list{position:absolute;top:92px;list-style:none;font-size:14px;line-height:26px;color:var(--footer-text)}
.foot-list li::before{content:"›";display:inline-block;width:12px;color:#888}
.contact-line{position:absolute;left:615px;font-size:14px;color:var(--footer-text);line-height:22px}
.contact-phone{position:absolute;left:614px;top:162px;font-size:17px;font-weight:600;color:#ddd}
.contact-icon{position:absolute;left:588px}
.site-footer .brand{left:828px;top:128px;gap:26px}
.site-footer .brand-dot{width:46px;height:46px}
.site-footer .brand-name{font-size:40px;color:#9a9a9a}
.footer-bottom{position:absolute;left:0;top:1318px;width:1200px;height:59px;background:var(--footer-bottom);font-size:13.5px;color:#ccc}
.footer-bottom span{position:absolute;top:22px}
</style>
</head>
<body>
<div class="page">

  <header class="site-header">
    <div class="brand"><div class="brand-dot"></div><div class="brand-name">Bellmoran</div></div>
    <div class="call">
      <svg width="44" height="46" viewBox="0 0 44 46" aria-hidden="true">
        <path d="M6 4c3-2 6-1 7 2l3 7c1 2 0 4-2 5l-3 2c2 6 6 10 11 13l2-3c1-2 3-3 5-2l7 3c3 1 3 4 2 7l-3 4c-3 3-9 3-15-1C13 36 6 27 3 18 1 11 2 7 6 4z" fill="#111"/>
        <path d="M26 8a12 12 0 0 1 10 10M28 2a18 18 0 0 1 14 14" stroke="var(--green)" stroke-width="3" fill="none" stroke-linecap="round"/>
      </svg>
      <div class="call-label">CALL US TODAY</div>
      <div class="call-number">555-210-48260</div>
    </div>
  </header>

  <nav class="main-nav">
    <div class="nav-item active">Home</div>
    <div class="nav-sep" style="left:186px"></div>
    <div class="nav-item" style="left:212px">Services</div>
    <div class="nav-sep" style="left:293px"></div>
    <div class="nav-item" style="left:319px">Wind Farms</div>
    <div class="nav-sep" style="left:427px"></div>
    <div class="nav-item" style="left:453px">Projects</div>
    <div class="nav-sep" style="left:536px"></div>
    <div class="nav-item" style="left:559px">About</div>
    <div class="nav-sep" style="left:626px"></div>
    <div class="nav-item" style="left:651px">Contact</div>
    <div class="follow">Follow Us</div>
    <div class="social" style="left:980px" aria-label="Social profile"></div>
    <div class="social" style="left:1020px" aria-label="chirpnet"></div>
    <div class="social" style="left:1060px" aria-label="workgrid"></div>
  </nav>

  <section class="hero" role="img" aria-label="Rows of wind turbines silhouetted against a sunset sky">
    <h1 class="hero-title">WE ARE A <b>RENEWABLE ENERGY</b><br>FOCUSSED CONSULTANCY</h1>
  </section>

  <!-- who we are -->
  <h2 class="section-title" style="left:118px"><span>Who</span> We Are</h2>
  <div class="section-rule" style="left:118px;width:296px"></div>
  <div class="photo" style="left:118px;top:737px;width:294px;height:154px;border:1px solid #e2e2e2;box-shadow:0 1px 3px rgba(0,0,0,.15);background:#fff"></div>
  <div class="photo" role="img" aria-label="Wind turbines above a field with hay bales" style="left:125px;top:743px;width:279px;height:140px;background:linear-gradient(180deg,#7fb0de 0%,#b7d3ea 60%,#8e8a5e 80%,#5e5a3c 100%)"></div>
  <p class="body-copy" style="left:122px;top:899px;width:285px">Lorem Ipsum is simply dummy text of the printing and typesetting industry. Lorem Ipsum has been the industry's and.</p>
  <div class="btn">Read More</div>

  <!-- blog -->
  <h2 class="section-title" style="left:437px"><span>From</span> The Blog</h2>
  <div class="section-rule" style="left:437px;width:280px"></div>
  <h3 class="post-title" style="top:740px">Lorem Ipsum Dolor Sit</h3>
  <p class="body-copy" style="left:437px;top:772px;width:312px">Lorem Ipsum is simply dummy text of the print-ing and typesetting industry. Lorem Ipsum has been the industry's standar</p>
  <a class="read-more" style="top:842px">Read More</a>
  <h3 class="post-title" style="top:880px">Lorem Ipsum Dolor Sit</h3>
  <p class="body-copy" style="left:437px;top:914px;width:312px">Lorem Ipsum is simply dummy text of the print-ing and typesetting industry. Lorem Ipsum has been the industry's standar</p>
  <a class="read-more" style="top:987px">Read More</a>

  <!-- projects -->
  <h2 class="section-title" style="left:763px"><span>Our</span> Projects</h2>
  <div class="section-rule" style="left:763px;width:320px"></div>
  <div class="project-card"></div>
  <div class="photo" role="img" aria-label="Offshore installation vessel carrying wind turbine blades" style="left:767px;top:741px;width:317px;height:121px;background:linear-gradient(180deg,#8ea2b8 0%,#c9cfd6 50%,#6e6a66 80%,#b2302a 100%)"></div>
  <div class="project-title">Lorem Ipsum Dolor Sit amet Type</div>
  <p class="body-copy" style="left:779px;top:901px;width:290px">Lorem Ipsum is simply dummy text of the printing and typesetting industry.</p>
  <div class="pager">
    <div class="arrow"><svg width="12" height="14" viewBox="0 0 12 14"><path d="M9 1 3 7l6 6" stroke="#ccc" stroke-width="2.5" fill="none"/></svg></div>
    <div class="num current">1</div><div class="num">2</div><div class="num">3</div><div class="num">4</div><div class="num">5</div>
    <div class="arrow"><svg width="12" height="14" viewBox="0 0 12 14"><path d="M3 1l6 6-6 6" stroke="#ccc" stroke-width="2.5" fill="none"/></svg></div>
  </div>

  <footer class="site-footer">
    <h4 class="foot-title" style="left:116px">Who We Are</h4>
    <div class="foot-rule" style="left:118px;width:176px"></div>
    <ul class="foot-list" style="left:118px">
      <li>Home</li><li>Gallery</li><li>Services</li><li>Warranty</li><li>Contact</li>
    </ul>

    <h4 class="foot-title" style="left:324px">Our Services</h4>
    <div class="foot-rule" style="left:326px;width:216px"></div>
    <ul class="foot-list" style="left:326px">
      <li>Lorem Ipsum Dolor Sit Amet</li><li>Typesetting Industry</li><li>Have been Sent in Lorem</li><li>Services Which Done</li><li>Inside Vehicula Quis</li>
    </ul>

    <h4 class="foot-title" style="left:586px">Contact Us</h4>
    <div class="foot-rule" style="left:588px;width:216px"></div>
    <svg class="contact-icon" style="top:92px" width="14" height="19" viewBox="0 0 14 19" aria-hidden="true"><path d="M7 0a7 7 0 0 1 7 7c0 5-7 12-7 12S0 12 0 7a7 7 0 0 1 7-7z" fill="#888"/><circle cx="7" cy="7" r="2.5" fill="var(--footer)"/></svg>
    <p class="contact-line" style="top:91px">4820 Ridgeline Road 17<br>Cedar Hollow, Alberta<br>T2K 4P9</p>
    <svg class="contact-icon" style="top:160px" width="18" height="20" viewBox="0 0 18 20" aria-hidden="true"><path d="M3 1c2-1 3 0 4 1l1 4c0 1 0 2-1 2l-1 1c1 3 3 5 5 6l1-1c1-1 2-1 3 0l2 2c1 1 1 2 0 3-2 2-6 1-9-2S0 7 1 4z" fill="#888"/></svg>
    <div class="contact-phone">555-210-4826</div>
    <svg class="contact-icon" style="top:201px" width="20" height="14" viewBox="0 0 20 14" aria-hidden="true"><rect x="0.5" y="0.5" width="19" height="13" fill="none" stroke="#888"/><path d="M1 1l9 7 9-7M1 13l7-6M19 13l-7-6" stroke="#888" fill="none"/></svg>
    <p class="contact-line" style="top:196px">info@bellmoran.com</p>

    <div class="brand"><div class="brand-dot"></div><div class="brand-name">Bellmoran</div></div>
  </footer>

  <div class="footer-bottom">
    <span style="left:115px">copyright©2015.Bellmoran. All Rights Reserved</span>
    <span style="left:853px">Privacy Policy</span>
    <span style="left:950px;color:#777">|</span>
    <span style="left:969px">Terms &amp; Conditions</span>
  </div>

</div>
</body>
</html>
```